New Church Home Page and Content Page Design

Our church, Cedar Hollow Baptist Church www.chbcfenway.example, needs an update for our online presence. The homepage design should provide the following 4 pieces of information above the fold:
1. Church location - 47 Linden Brook Lane in Chappaqua, NY, USA.
2. Service times and types Sunday school, children's church, etc..
3. A space for some text describing us and our beliefs - a Bible believing independent Baptist church.
4. photos of our members to give visitors an impression of what kind of people attend our church - a friendly group of culturally diverse people who love Jesus.

In addition to the homepage we need a design for internal pages of general content. The content page design should provide a lot of room for content and prominent navigation area. We will use this design to host pages with content such as:
A full description of our beliefs
A photo gallery
An event calendar
Embedded audio and video of past sermons
A member directory
etc.
Updates

Thanks everyone for your submissions. I'll be meeting with our Pastor tomorrow. I am working as fast as I can to review all the designs and come up with a short list for him. A decision should be close behind.

Target Market(s)

Local people looking for a church.

Industry/Entity Type

Church

Requirements
Must have
• 1. Place to show church location - Westchester county, New York State, USA.
2. Place to list service times and types.
3. A space for some text describing us and our beliefs.
4. A place to display photos of our members (see also the nice to have section)
Nice to have
• Would be great if the member photos (#4 in must have section) displayed the images in some innovative way. I rather not have an ordinary carousel of images.

```html
<!DOCTYPE html>
<html lang="en">
<head>
<meta charset="utf-8">
<title>Cedar Hollow Baptist Church – Home</title>
<link href="https://fonts.googleapis.com/css2?family=Open+Sans:wght@400;600;700&display=swap" rel="stylesheet">
<style>
:root{
  --navy:#1b3a5c;
  --navy-dark:#132b45;
  --blue:#2a5a8a;
  --blue-light:#3d74a8;
  --band:#e6e8ea;
  --footer:#c9d6e2;
  --text:#333;
  --muted:#777;
  --line:#d5d8db;
  --white:#fff;
}
*{box-sizing:border-box;margin:0;padding:0}
html,body{width:1200px;height:2596px;overflow:hidden}
body{font-family:'Open Sans',Arial,sans-serif;color:var(--text);background:var(--white);position:relative;font-size:14px}
.wrap{position:absolute;left:112px;width:976px}
.topbar{position:absolute;top:0;left:0;width:1200px;height:48px;background:var(--navy-dark);color:#dce5ee;font-size:13px}
.topbar .addr{position:absolute;left:112px;top:15px;display:flex;gap:8px;align-items:center}
.topbar .contact{position:absolute;right:112px;top:12px;display:flex;gap:8px;align-items:center}
.sq{width:22px;height:22px;background:#3b5c80;border-radius:3px;display:inline-block}
.header{top:48px;height:112px}
.brand{position:absolute;left:0;top:24px;display:flex;align-items:center;gap:14px}
.brand-mark{width:54px;height:54px;background:var(--navy)}
.brand-name{font-weight:700;font-size:20px;line-height:22px;color:var(--navy);width:170px}
.services{position:absolute;left:540px;top:34px;width:180px;text-align:center;font-size:14px;color:var(--navy);line-height:20px}
.services b{font-weight:700}
.search{position:absolute;right:0;top:38px;display:flex}
.search span{width:190px;height:32px;border:1px solid var(--line);font-size:12px;color:#999;padding:7px 10px}
.search i{width:40px;height:32px;background:var(--navy);display:flex;align-items:center;justify-content:center}
.nav{position:absolute;top:160px;left:0;width:1200px;height:48px;background:var(--navy)}
.nav ul{list-style:none;display:flex;position:absolute;left:112px;height:48px}
.nav li{color:#fff;font-size:13px;padding:0 18px;line-height:48px}
.nav li.active{background:var(--blue-light)}
.stage{position:absolute;top:208px;left:0;width:1200px;height:576px;background:var(--navy)}
.hero{top:220px;height:360px;background:linear-gradient(100deg,#cfc9bd 0%,#a89c88 45%,#5b4a38 100%)}
.hero h1{position:absolute;left:32px;top:70px;font-size:27px;font-weight:600;color:#fff}
.hero p{position:absolute;left:32px;top:116px;font-size:14px;color:#fff;line-height:26px;width:520px}
.features{top:608px;height:152px}
.feature{position:absolute;top:0;width:288px;height:152px;background:linear-gradient(135deg,#8fa5bb,#54708e)}
.feature .label{position:absolute;left:0;bottom:0;width:100%;height:58px;background:rgba(27,58,92,.85);text-align:center;color:#fff}
.feature h3{font-size:16px;font-weight:600;margin-top:4px}
.btn{display:inline-block;background:var(--navy-dark);color:#fff;font-size:12px;padding:3px 14px;border-radius:2px;margin-top:2px}
.section-title{font-size:20px;font-weight:600;color:var(--navy);padding-bottom:8px;border-bottom:2px solid var(--line)}
.members{top:800px}
.cards{position:relative;height:200px;margin-top:20px}
.card{position:absolute;top:0;width:232px;text-align:center}
.card .photo{height:178px;background:linear-gradient(160deg,#b5a48c,#6d5a49)}
.card h4{font-size:14px;font-weight:600;margin-top:6px;color:var(--navy)}
.card p{font-size:11px;color:var(--muted)}
.band{position:absolute;top:1130px;left:0;width:1200px;height:390px;background:var(--band)}
.col{position:absolute;top:1150px}
.col h2{font-size:18px;font-weight:600;color:var(--navy);margin-bottom:12px}
.player{height:36px;background:#222;border-radius:3px;display:flex;align-items:center;padding:0 10px;gap:8px}
.player .bar{flex:1;height:4px;background:#666}
.video{height:150px;background:linear-gradient(135deg,#333,#111)}
.news-item{display:flex;gap:10px;margin-bottom:14px}
.news-item .thumb{width:62px;height:52px;background:linear-gradient(135deg,#999,#555);flex:none}
.news-item p{font-size:11px;color:#555;line-height:15px}
.cal{background:#fff;border:1px solid var(--line)}
.cal-head{display:flex;justify-content:space-between;align-items:center;background:#eee;padding:6px 10px;font-size:14px;font-weight:600}
.cal table{width:100%;border-collapse:collapse;font-size:12px;text-align:center}
.cal th{font-weight:600;padding:6px 0;color:#555}
.cal td{padding:7px 0;border-top:1px solid #eee;color:#444}
.cal td.off{color:#bbb}
.cal td.on{background:var(--blue);color:#fff}
.gallery{top:1546px}
.tile{position:absolute;background:linear-gradient(150deg,#8aa67a,#3f5c3b)}
.tile .cap{position:absolute;left:0;bottom:0;width:100%;background:rgba(40,40,40,.8);color:#fff;font-size:14px;padding:8px 12px;line-height:18px}
.footer{position:absolute;top:2100px;left:0;width:1200px;height:448px;background:var(--footer)}
.fcol{position:absolute;top:2150px;font-size:11px;color:#3c4d5e;line-height:16px}
.fcol h5{font-size:12px;font-weight:700;color:var(--navy);margin-bottom:12px}
.post{display:flex;gap:8px;margin-bottom:14px}
.post .thumb{width:44px;height:40px;background:linear-gradient(135deg,#9a8c7a,#5e5145);flex:none}
.field{height:26px;background:#fff;border:1px solid #aab8c6;margin:4px 0 10px}
.sign{display:inline-block;background:var(--navy);color:#fff;padding:4px 14px;font-size:11px}
.copy{position:absolute;top:2548px;left:0;width:1200px;height:48px;background:var(--navy-dark);color:#dce5ee;font-size:12px;text-align:center;line-height:48px}
</style>
</head>
<body>

<div class="topbar">
  <div class="addr">
    <svg width="12" height="16" viewBox="0 0 12 16"><path d="M6 0a6 6 0 0 0-6 6c0 4.5 6 10 6 10s6-5.5 6-10a6 6 0 0 0-6-6zm0 8.5A2.5 2.5 0 1 1 6 3.5a2.5 2.5 0 0 1 0 5z" fill="#dce5ee"/></svg>
    Cedar Hollow Baptist Church 47 Linden Brook Lane, Alder Springs, NY 10599
  </div>
  <div class="contact">
    <svg width="14" height="14" viewBox="0 0 14 14"><path d="M3 1l2 3-1.5 1.5a8 8 0 0 0 5 5L10 9l3 2-1.5 2.5C6 13 1 8 .5 2.5z" fill="#dce5ee"/></svg>
    <span>914-555-0182</span>
    <span class="sq"></span><span class="sq"></span><span class="sq"></span><span class="sq"></span>
  </div>
</div>

<header class="wrap header">
  <div class="brand">
    <span class="brand-mark"></span>
    <span class="brand-name">Cedar Hollow Baptist Church</span>
  </div>
  <div class="services"><b>Sunday Services</b><br>@ 9:30 &amp; 11:00 am</div>
  <div class="search">
    <span>Search...</span>
    <i><svg width="16" height="16" viewBox="0 0 16 16"><circle cx="6.5" cy="6.5" r="5" stroke="#fff" stroke-width="2" fill="none"/><path d="M10 10l5 5" stroke="#fff" stroke-width="2"/></svg></i>
  </div>
</header>

<nav class="nav">
  <ul>
    <li class="active">Home</li><li>Calendar</li><li>Ministries</li><li>Service Times</li><li>Sermons and Media</li><li>Contact Us</li>
  </ul>
</nav>

<div class="stage"></div>

<section class="wrap hero" role="img" aria-label="Open Bible with a wooden cross resting on its pages">
  <h1>Welcome To Cedar Hollow Baptist Church</h1>
  <p>We Are Glad You Are Here Our Mission Is to Guide People Of All Backgrounds Into A Personal Relationship With Jesus Christ</p>
</section>

<section class="wrap features">
  <div class="feature" style="left:0" role="img" aria-label="Members gathered in a fellowship group">
    <div class="label"><h3>Fellowship Groups</h3><span class="btn">View Group</span></div>
  </div>
  <div class="feature" style="left:344px" role="img" aria-label="Two hands meeting in a welcoming handshake">
    <div class="label"><h3>Your First Visit</h3><span class="btn">Read More</span></div>
  </div>
  <div class="feature" style="left:688px" role="img" aria-label="A child smiling at a church event">
    <div class="label"><h3>Every Penny Helps</h3><span class="btn">Donate Now</span></div>
  </div>
</section>

<section class="wrap members">
  <h2 class="section-title">Our Members</h2>
  <div class="cards">
    <div class="card" style="left:0"><div class="photo" role="img" aria-label="Portrait of the church father"></div><h4>Father</h4><p>Lorem Ipsum Dolor</p></div>
    <div class="card" style="left:248px"><div class="photo" role="img" aria-label="Portrait of a sister of the church"></div><h4>Sister</h4><p>Lorem Ipsum Dolor</p></div>
    <div class="card" style="left:496px"><div class="photo" role="img" aria-label="Portrait of a church pastor"></div><h4>Pastor</h4><p>Lorem Ipsum Dolor</p></div>
    <div class="card" style="left:744px"><div class="photo" role="img" aria-label="Portrait of a church pastor"></div><h4>Pastor</h4><p>Lorem Ipsum Dolor</p></div>
  </div>
</section>

<div class="band"></div>

<section class="col" style="left:112px;width:280px">
  <h2>Listen to Podcasts</h2>
  <div class="player">
    <svg width="10" height="12" viewBox="0 0 10 12"><path d="M0 0l10 6-10 6z" fill="#fff"/></svg>
    <span class="bar"></span>
  </div>
  <h2 style="margin-top:22px">Featured Video</h2>
  <div class="video" role="img" aria-label="Still frame from the featured sermon video"></div>
  <div class="player" style="border-radius:0 0 3px 3px">
    <svg width="10" height="12" viewBox="0 0 10 12"><path d="M0 0l10 6-10 6z" fill="#fff"/></svg>
    <span class="bar"></span>
  </div>
</section>

<section class="col" style="left:432px;width:248px">
  <h2>Latest News</h2>
  <p style="font-size:12px;color:#555;margin-bottom:10px">Default News Post</p>
  <div class="news-item"><div class="thumb" role="img" aria-label="News photo"></div><p>Our spring fellowship dinner brings families together for a warm evening of food, song and prayer.</p></div>
  <p style="font-size:12px;color:#555;margin-bottom:10px">Lorem ipsum dolor sit amet</p>
  <div class="news-item"><div class="thumb" role="img" aria-label="News photo"></div><p>Volunteers are needed for the summer Bible school program. Sign up after Sunday service.</p></div>
</section>

<section class="col" style="left:712px;width:376px">
  <h2>Upcoming Events</h2>
  <div class="cal">
    <div class="cal-head"><span>&#8249;</span><span>April 2014</span><span>&#8250;</span></div>
    <table>
      <tr><th>Sun</th><th>Mon</th><th>Tue</th><th>Wed</th><th>Thu</th><th>Fri</th><th>Sat</th></tr>
      <tr><td class="off">30</td><td class="off">31</td><td>1</td><td>2</td><td>3</td><td>4</td><td>5</td></tr>
      <tr><td>6</td><td>7</td><td>8</td><td>9</td><td>10</td><td>11</td><td>12</td></tr>
      <tr><td>13</td><td>14</td><td>15</td><td>16</td><td>17</td><td>18</td><td>19</td></tr>
      <tr><td>20</td><td>21</td><td>22</td><td class="on">23</td><td>24</td><td>25</td><td>26</td></tr>
      <tr><td>27</td><td>28</td><td>29</td><td>30</td><td class="off">1</td><td class="off">2</td><td class="off">3</td></tr>
      <tr><td class="off">4</td><td class="off">5</td><td class="off">6</td><td class="off">7</td><td class="off">8</td><td class="off">9</td><td class="off">10</td></tr>
    </table>
  </div>
</section>

<section class="wrap gallery">
  <h2 class="section-title">Photo Gallery</h2>
  <div style="position:relative;height:460px;margin-top:28px">
    <div class="tile" style="left:0;top:0;width:480px;height:460px" role="img" aria-label="Couple standing before the church sign"><div class="cap">Lorem ipsum dolor sit amet<br>Lorem ipsum dolor</div></div>
    <div class="tile" style="left:496px;top:0;width:232px;height:222px" role="img" aria-label="Members greeting each other"><div class="cap">Lorem ipsum dolor<br>sit amet conse</div></div>
    <div class="tile" style="left:744px;top:0;width:232px;height:222px" role="img" aria-label="Family at an outdoor gathering"><div class="cap">Lorem ipsum dolor<br>sit amet con</div></div>
    <div class="tile" style="left:496px;top:238px;width:232px;height:222px" role="img" aria-label="Church picnic pavilion"><div class="cap">Lorem ipsum dolor<br>sit amet</div></div>
    <div class="tile" style="left:744px;top:238px;width:232px;height:222px" role="img" aria-label="Young members outdoors"><div class="cap">Lorem ipsum dolor<br>sit amet</div></div>
  </div>
</section>

<footer class="footer"></footer>

<div class="fcol" style="left:112px;width:200px">
  <h5>ABOUT OUR CHURCH</h5>
  <p>We are a Bible believing independent Baptist church welcoming every neighbor to worship, grow and serve with us.</p>
  <h5 style="margin-top:16px">VISIT US</h5>
  <p>47 Linden Brook Lane<br>Alder Springs, NY 10599</p>
  <p style="margin-top:6px">914-555-0182</p>
  <p style="margin-top:6px">hello@cedarhollowworship.example</p>
  <div style="display:flex;gap:6px;margin-top:14px"><span class="sq" style="border-radius:50%"></span><span class="sq" style="border-radius:50%"></span><span class="sq" style="border-radius:50%"></span><span class="sq" style="border-radius:50%"></span></div>
</div>

<div class="fcol" style="left:368px;width:190px">
  <h5>RECENT POSTS</h5>
  <div class="post"><div class="thumb" role="img" aria-label="Post photo"></div><p>Easter week schedule<br>Apr 12, 2014 | 3 Comments</p></div>
  <div class="post"><div class="thumb" role="img" aria-label="Post photo"></div><p>Youth choir returns<br>Apr 10, 2014 | 2 Comments</p></div>
  <div class="post"><div class="thumb" role="img" aria-label="Post photo"></div><p>Mission trip update<br>Apr 08, 2014 | 4 Comments</p></div>
</div>

<div class="fcol" style="left:620px;width:190px">
  <h5>RECENT NEWS</h5>
  <p>New Sunday school classes</p><p style="margin-top:6px">Food pantry drive results</p><p style="margin-top:6px">Men's breakfast this Saturday</p><p style="margin-top:6px">Women's prayer circle</p><p style="margin-top:6px">Welcome our new deacons</p><p style="margin-top:6px">Spring baptism service</p>
</div>

<div class="fcol" style="left:872px;width:216px">
  <h5>NEWSLETTER SUBSCRIPTION</h5>
  <p>Sign up to receive church news, events and weekly devotions by email.</p>
  <p style="margin-top:10px">Your Name*</p><div class="field"></div>
  <p>Your Email Address*</p><div class="field"></div>
  <span class="sign">Sign up</span>
</div>

<div class="copy">Copyright © 2014 Cedar Hollow Baptist Church</div>

</body>
</html>
```